Business Card Design Project

2 sided business card utilizing existing logo
- English on one side, Arabic on the other side (both English and Arabic text will be provided)
Same color scheme as logo
Information included will be: name, title, email, phone, address and website (www.dravelnix.com)
Updates

Target Market(s)

We are a Systems Integration Company

Industry/Entity Type

Business

Font styles to use
Serif
Sans Serif

Requirements
Should not have
• We prefer using the flat logo rather than one with shadow/3D effect

```html
<!DOCTYPE html>
<html lang="en">
<head>
<meta charset="utf-8">
<title>Dravelnix Business Card</title>
<link rel="stylesheet" href="https://fonts.googleapis.com/css2?family=Questrial&display=swap">
<style>
  :root {
    --stage: #bcbcbc;
    --card-white: #ffffff;
    --brand-red: #e31e24;
    --brand-red-dark: #b5161b;
    --card-black: #121212;
    --card-black-top: #1f1f1f;
    --text-light: #ffffff;
    --divider: #8a8a8a;
  }
  * { box-sizing: border-box; margin: 0; padding: 0; }
  html, body {
    width: 1200px; height: 900px; overflow: hidden;
    background: var(--stage);
    font-family: "Questrial", "Century Gothic", sans-serif;
  }
  .card {
    position: absolute; left: 150px; top: 193px;
    width: 900px; height: 514px;
    border-radius: 34px; overflow: hidden;
    background: var(--card-white);
  }
  .brand {
    position: absolute; left: 0; right: 0; top: 0; height: 296px;
    display: flex; align-items: center; justify-content: center; gap: 18px;
  }
  .brand-mark {
    width: 30px; height: 30px; background: var(--brand-red);
  }
  .brand-name {
    color: var(--brand-red); font-size: 58px; letter-spacing: 9px;
  }
  .accent-band {
    position: absolute; left: 0; right: 0; top: 296px; height: 22px;
    background: linear-gradient(var(--brand-red), var(--brand-red-dark));
  }
  .info-panel {
    position: absolute; left: 0; right: 0; top: 318px; bottom: 0;
    background: linear-gradient(var(--card-black-top), var(--card-black));
  }
  .holder {
    position: absolute; right: 445px; top: 38px; text-align: right;
  }
  .holder-name { color: var(--brand-red); font-size: 33px; }
  .holder-title { color: var(--text-light); font-size: 25px; margin-top: 4px; }
  .divider {
    position: absolute; left: 475px; top: 16px; width: 2px; height: 160px;
    background: var(--divider);
  }
  .contacts {
    position: absolute; left: 498px; top: 16px; list-style: none;
    color: var(--text-light); font-size: 23px; line-height: 31px;
  }
  .contacts li { display: flex; align-items: flex-start; gap: 8px; }
  .contacts svg { width: 26px; height: 26px; margin-top: 3px; flex: none; fill: var(--brand-red); }
</style>
</head>
<body>
  <div class="card">
    <div class="brand">
      <span class="brand-mark"></span>
      <span class="brand-name">DRAVELNIX</span>
    </div>
    <div class="accent-band"></div>
    <div class="info-panel">
      <div class="holder">
        <p class="holder-name">Marek Tolland</p>
        <p class="holder-title">manager</p>
      </div>
      <div class="divider"></div>
      <ul class="contacts">
        <li>
          <svg viewBox="0 0 24 24"><path d="M6.6 10.8a15.1 15.1 0 0 0 6.6 6.6l2.2-2.2a1 1 0 0 1 1-.25 11.4 11.4 0 0 0 3.6.57 1 1 0 0 1 1 1V20a1 1 0 0 1-1 1A17 17 0 0 1 3 4a1 1 0 0 1 1-1h3.5a1 1 0 0 1 1 1c0 1.25.2 2.45.57 3.57a1 1 0 0 1-.25 1z"/></svg>
          <span>(916) 555-0142</span>
        </li>
        <li>
          <svg viewBox="0 0 24 24"><path d="M2 8l10 6 10-6v11H2z"/><path d="M2 6h20l-10 6z"/></svg>
          <span>info@dravelnix.com</span>
        </li>
        <li>
          <svg viewBox="0 0 24 24"><path d="M12 2a10 10 0 1 0 0 20 10 10 0 0 0 0-20zm6.9 6h-2.9a15 15 0 0 0-1.3-3.6A8 8 0 0 1 18.9 8zM12 4.1c.8 1.1 1.5 2.4 1.9 3.9h-3.8c.4-1.5 1.1-2.8 1.9-3.9zM4.3 14a8 8 0 0 1 0-4h3.3a16 16 0 0 0 0 4zm.8 2h2.9a15 15 0 0 0 1.3 3.6A8 8 0 0 1 5.1 16zM8 8H5.1a8 8 0 0 1 4.2-3.6A15 15 0 0 0 8 8zm4 11.9c-.8-1.1-1.5-2.4-1.9-3.9h3.8c-.4 1.5-1.1 2.8-1.9 3.9zM14.3 14H9.7a14 14 0 0 1 0-4h4.6a14 14 0 0 1 0 4zm.4 5.6A15 15 0 0 0 16 16h2.9a8 8 0 0 1-4.2 3.6zm1.7-5.6a16 16 0 0 0 0-4h3.3a8 8 0 0 1 0 4z"/></svg>
          <span>www.dravelnix.com</span>
        </li>
        <li>
          <svg viewBox="0 0 24 24"><path d="M12 3L1 12h3v9h6v-6h4v6h6v-9h3z"/></svg>
          <span>4172 Larkspur Avenue, Suite D,<br>Maple Grove, CA 95830</span>
        </li>
      </ul>
    </div>
  </div>
</body>
</html>
```